Brochure Design Project - Brisk Chiller

We need a brochure redesign to change the branding of the cooler unit from our Hong Kong distributors marketing to a more European/Australian/American friendly aesthetic.

We would like to see designs which communicate clearly and effectively the purpose of the product and the ease of use.

Feel free to modify the colour of the cooler unit so it works with the brochure.

Target Market(s)

Commercial Users and Hire Companies in Australia

Industry/Entity Type

Marketing

Requirements
Must have
• - Two sided A4 Portrait (More pages if reqd is OK)
- A clear list of specifications either in a table or sentence format
- Specifications from current brochure
- Highlight CE Certification
- Highlight Full Product Two Year Commercial Warranty
- Efficient and Environmentally Friendly Cooling
- Contact Details Panel with contact phone number and address to be edited later

```html
<!DOCTYPE html>
<html lang="en">
<head>
<meta charset="utf-8">
<title>Brisk Chiller – Evaporative Cooler Brochure</title>
<link href="https://fonts.googleapis.com/css2?family=Raleway:wght@400;600&family=Oswald:wght@500&family=Roboto:wght@400;500&display=swap" rel="stylesheet">
<style>
  :root {
    --sky: #3cc3f0;
    --white: #ffffff;
    --ink: #1d1d1d;
    --navy: #1b4f7a;
    --photo-grey-a: #6f7175;
    --photo-grey-b: #4a4c50;
    --photo-tan-a: #b99584;
    --photo-tan-b: #8e6c5d;
  }
  * { margin: 0; padding: 0; box-sizing: border-box; }
  html, body { width: 1200px; height: 1000px; overflow: hidden; background: var(--white); }
  .canvas { position: relative; width: 1200px; height: 1000px; font-family: "Raleway", sans-serif; }
  .shapes { position: absolute; inset: 0; }
  .abs { position: absolute; }

  /* front page */
  .brand {
    left: 110px; top: 140px; width: 232px; height: 66px;
    border: 1.5px solid var(--ink); border-radius: 12px;
    display: flex; align-items: center; justify-content: center;
    font-family: "Raleway", sans-serif; font-weight: 600; font-size: 34px; color: var(--ink);
  }
  .warranty {
    left: 372px; top: 188px; width: 165px;
    font-family: "Oswald", sans-serif; font-weight: 500; font-size: 16px; line-height: 21px;
    color: var(--sky); text-align: center;
  }
  .title {
    left: 146px; top: 290px; transform: rotate(12deg); transform-origin: left top;
    font-family: "Raleway", sans-serif; font-weight: 600; font-size: 31px; color: var(--white); letter-spacing: 1px;
    white-space: nowrap;
  }
  .pill {
    background: var(--white); border: 4px solid var(--sky); border-radius: 14px;
    color: var(--sky); font-weight: 600; white-space: nowrap;
    box-shadow: 0 0 0 3px var(--white);
  }
  .features-pill { left: 52px; top: 392px; padding: 6px 14px; font-size: 29px; transform: rotate(11deg); transform-origin: left top; }
  .features {
    left: 72px; top: 468px; width: 180px; transform: rotate(11deg); transform-origin: left top;
    list-style: none; font-family: "Roboto", sans-serif; font-size: 10.5px; line-height: 12px; color: var(--white);
  }
  .features li { margin-bottom: 10px; }
  .ce-pill { left: 268px; top: 728px; padding: 6px 16px; font-size: 24px; transform: rotate(10deg); transform-origin: left top; }
  .ce-note {
    left: 218px; top: 800px; transform: rotate(8deg); transform-origin: left top;
    font-family: "Roboto", sans-serif; font-size: 11px; color: var(--navy); white-space: nowrap;
  }
  .footnote {
    left: 30px; top: 864px; width: 245px; transform: rotate(9deg); transform-origin: left top;
    font-family: "Roboto", sans-serif; font-size: 10.5px; line-height: 12px; color: var(--sky);
  }

  /* back page */
  .spec-pill { left: 712px; top: 612px; padding: 6px 36px; font-size: 16px; transform: rotate(3deg); transform-origin: left top; }
  .spec {
    left: 640px; top: 666px; transform: rotate(3deg); transform-origin: left top;
    display: grid; grid-template-columns: 108px 220px; column-gap: 32px;
    font-family: "Roboto", sans-serif; font-size: 14px; line-height: 19px; color: var(--white);
  }
  .spec dt { text-align: right; font-weight: 400; }
  .spec dd { font-weight: 500; }
  .contact-title { left: 1054px; top: 662px; font-size: 15px; color: var(--sky); transform: rotate(3deg); transform-origin: left top; white-space: nowrap; }
  .contact-icons { left: 1056px; top: 700px; display: flex; flex-direction: column; gap: 20px; }
  .tagline {
    left: 640px; top: 842px; transform: rotate(3deg); transform-origin: left top;
    font-size: 20px; color: var(--sky); white-space: nowrap;
  }
</style>
</head>
<body>
<div class="canvas">

  <svg class="shapes" width="1200" height="1000" viewBox="0 0 1200 1000">
    <defs>
      <linearGradient id="grey-unit" x1="0" y1="0" x2="1" y2="1">
        <stop offset="0" stop-color="var(--photo-grey-a)"/>
        <stop offset="1" stop-color="var(--photo-grey-b)"/>
      </linearGradient>
      <linearGradient id="tan-unit" x1="0" y1="0" x2="1" y2="1">
        <stop offset="0" stop-color="var(--photo-tan-a)"/>
        <stop offset="1" stop-color="var(--photo-tan-b)"/>
      </linearGradient>
    </defs>

    <!-- front page bands -->
    <polygon fill="var(--sky)" points="20,185 365,262 395,115 575,115 575,905 400,905 20,840"/>
    <polygon fill="var(--white)" points="20,252 575,328 575,340 20,264"/>
    <polygon fill="var(--white)" points="300,398 575,462 575,758 232,698"/>
    <circle cx="455" cy="228" r="82" fill="var(--white)"/>
    <rect role="img" aria-label="Photo of the grey evaporative cooler unit on castor wheels" x="340" y="448" width="170" height="282" rx="30" fill="url(#grey-unit)"/>

    <!-- back page bands -->
    <polygon fill="var(--sky)" points="628,110 1187,110 1187,905 1070,905 1070,838 628,828"/>
    <polygon fill="var(--white)" points="628,828 1070,838 1070,905 628,895"/>
    <polygon fill="var(--white)" points="630,135 838,138 838,360 630,357"/>
    <polygon fill="var(--white)" points="876,110 1065,110 1065,376 876,360"/>
    <polygon fill="var(--white)" points="630,392 838,396 838,600 630,596"/>
    <polygon fill="var(--white)" points="862,402 1070,406 1070,612 862,604"/>
    <rect fill="var(--white)" x="1087" y="110" width="100" height="498"/>
    <polygon fill="var(--white)" points="1034,652 1187,652 1187,840 1034,834"/>

    <g role="img" aria-label="Product photos of the tan cooler from front, rear, back and side">
      <rect x="690" y="148" width="110" height="200" rx="18" fill="url(#tan-unit)"/>
      <rect x="902" y="150" width="108" height="205" rx="18" fill="url(#tan-unit)"/>
      <rect x="702" y="402" width="100" height="182" rx="16" fill="url(#tan-unit)"/>
      <rect x="918" y="412" width="100" height="188" rx="16" fill="url(#tan-unit)"/>
    </g>
    <g role="img" aria-label="Detail photos: cooling pad, water gauge, inlet valve and fan grille">
      <rect x="1093" y="132" width="80" height="92" fill="url(#tan-unit)"/>
      <rect x="1093" y="254" width="80" height="92" fill="url(#tan-unit)"/>
      <rect x="1093" y="376" width="80" height="88" fill="url(#tan-unit)"/>
      <rect x="1093" y="492" width="80" height="108" fill="url(#tan-unit)"/>
    </g>
  </svg>

  <div class="abs brand">Forgewell</div>
  <div class="abs warranty">Full Product<br>twoYear<br>Commercial Warranty</div>
  <div class="abs title">EVAPORATIVE COOLER</div>

  <div class="abs pill features-pill">Product Features</div>
  <ul class="abs features">
    <li>*3- step fan speed, very low power consumption</li>
    <li>*Extra large water tank with 200L for more than 12 working hours.</li>
    <li>*Temperature drop up to 6-9 C (Depending on humidity condition).</li>
    <li>*Integrated body with leak-proof &amp; high impact strength with standing plastic</li>
  </ul>

  <div class="abs pill ce-pill">CE Certified Product</div>
  <div class="abs ce-note">conforms to EMSD [Electrical Product (safty) Regulations]</div>
  <p class="abs footnote">Specifications may be changed without prior notice due to product improvement</p>

  <div class="abs pill spec-pill">SPECIFICATION</div>
  <dl class="abs spec">
    <dt>Dimention</dt><dd>L850 x W700 x H16509(mm)</dd>
    <dt>Fan Dia.</dt><dd>500mm</dd>
    <dt>Flow Rate</dt><dd>110M/Min(Max)</dd>
    <dt>Power Supply</dt><dd>220V 50Hz AC</dd>
    <dt>Motor Speed</dt><dd>(H) ; 500W @ 1360 rpm</dd>
    <dt></dt><dd>(M) ; 430W @ 1000 rpm</dd>
    <dt>Weight</dt><dd>(L) ; 385W @ 650 rpm</dd>
    <dt></dt><dd>65kg</dd>
  </dl>

  <div class="abs contact-title">Contact&nbsp; Details</div>
  <div class="abs contact-icons">
    <svg width="16" height="14" viewBox="0 0 16 14" aria-label="Email"><rect x="1" y="2" width="14" height="10" fill="none" stroke="var(--sky)" stroke-width="1.6"/><polyline points="1,2 8,8 15,2" fill="none" stroke="var(--sky)" stroke-width="1.6"/></svg>
    <svg width="16" height="16" viewBox="0 0 16 16" aria-label="Fax"><rect x="4" y="1" width="8" height="5" fill="none" stroke="var(--sky)" stroke-width="1.5"/><rect x="1" y="6" width="14" height="6" fill="var(--sky)"/><rect x="4" y="10" width="8" height="5" fill="var(--white)" stroke="var(--sky)" stroke-width="1.5"/></svg>
    <svg width="12" height="18" viewBox="0 0 12 18" aria-label="Mobile phone"><rect x="1" y="1" width="10" height="16" rx="2" fill="none" stroke="var(--sky)" stroke-width="1.6"/><rect x="3" y="3" width="6" height="8" fill="var(--sky)"/></svg>
  </div>

  <div class="abs tagline">Efficient and Environmentally Friendly Cooling</div>
</div>
</body>
</html>
```